The Copper Lantern is a traditional English pub serving a vast range of beers and real ales. It has a very conservative oulook. Something classy would work well. We have an in-house logo. I'm thinking of good quality card in say cream with matching compliment slips and headed paper and envelopes

Industry/Entity Type

Conservative

Contact Information for Business Card

Copper Lantern Public House
58 Mill Lane
Harrowmere
Westshire
TW9 3RK
Derek P Lowther - Proprietor
www.copperlanternvale.co.uk
Tel: 020 7946 0382
Mobile; 077009 00415

Requirements
Must have
• Cl design essential. Black text.

2 sets of business cards required. one set must have my name - Derek P Lowther - Proprietor and the second set should have - Maureen Fitch - General Manager

```html
<!DOCTYPE html>
<html lang="en">
<head>
<meta charset="utf-8">
<title>The Copper Lantern – Business Card</title>
<link href="https://fonts.googleapis.com/css2?family=Arimo:wght@400;700&display=swap" rel="stylesheet">
<style>
  :root {
    --backdrop: #ededed;
    --card: #ffffff;
    --band: #4a4a4a;
    --ink: #111111;
    --ink-soft: #2a2a2a;
    --icon: #6d6d6d;
    --social: #9a9a9a;
    --logo: #ffffff;
  }
  * { box-sizing: border-box; margin: 0; padding: 0; }
  html, body {
    width: 1200px;
    height: 800px;
    overflow: hidden;
    background: var(--backdrop);
    font-family: "Arimo", Arial, sans-serif;
  }
  .business-card {
    position: absolute;
    left: 150px;
    top: 127px;
    width: 900px;
    height: 546px;
    background: var(--card);
    box-shadow: 0 6px 18px rgba(0,0,0,0.18);
    overflow: hidden;
  }
  .brand-band {
    height: 222px;
    background: var(--band);
    display: flex;
    align-items: center;
    padding-left: 90px;
    gap: 28px;
  }
  .brand-mark {
    width: 118px;
    height: 118px;
    border-radius: 50%;
    background: var(--logo);
  }
  .brand-name {
    color: var(--logo);
    font-weight: 700;
    font-size: 54px;
    line-height: 1.0;
    letter-spacing: 2px;
    text-transform: uppercase;
  }
  .social-links {
    position: absolute;
    right: 46px;
    top: 244px;
    display: flex;
    gap: 6px;
  }
  .social-links span {
    width: 40px;
    height: 40px;
    border-radius: 6px;
    background: var(--social);
  }
  .contact-block {
    position: absolute;
    left: 180px;
    top: 262px;
    color: var(--ink);
  }
  .person-name {
    font-weight: 700;
    font-size: 32px;
    letter-spacing: 0.5px;
    text-transform: uppercase;
  }
  .person-role {
    font-size: 21px;
    margin: 4px 0 14px 22px;
    color: var(--ink-soft);
  }
  .contact-list {
    list-style: none;
    margin-left: 22px;
  }
  .contact-list li {
    display: flex;
    align-items: center;
    gap: 18px;
    font-size: 22px;
    height: 31px;
  }
  .contact-list svg {
    width: 22px;
    height: 22px;
    fill: none;
    stroke: var(--icon);
    stroke-width: 1.8;
  }
  .address {
    font-size: 24px;
    margin: 30px 0 0 62px;
  }
</style>
</head>
<body>
  <section class="business-card" aria-label="Business card for The Copper Lantern">
    <header class="brand-band">
      <div class="brand-mark" aria-hidden="true"></div>
      <div class="brand-name">Copper<br>Lantern</div>
    </header>

    <div class="social-links" aria-label="Social media links">
      <span></span><span></span><span></span><span></span>
    </div>

    <div class="contact-block">
      <h1 class="person-name">Derek P Lowther</h1>
      <p class="person-role">Proprietor</p>
      <ul class="contact-list">
        <li>
          <svg viewBox="0 0 24 24" aria-hidden="true"><path d="M4 9c0-3 3-4 8-4s8 1 8 4v2h-4V9H8v2H4z"/><path d="M6 12h12l1 7H5z"/></svg>
          020 7946 0382
        </li>
        <li>
          <svg viewBox="0 0 24 24" aria-hidden="true"><rect x="7" y="3" width="10" height="18" rx="2"/><line x1="11" y1="18" x2="13" y2="18"/></svg>
          077009 00415
        </li>
        <li>
          <svg viewBox="0 0 24 24" aria-hidden="true"><circle cx="12" cy="12" r="9"/><ellipse cx="12" cy="12" rx="4" ry="9"/><line x1="3" y1="12" x2="21" y2="12"/></svg>
          www.copperlanternvale.co.uk
        </li>
      </ul>
      <p class="address">58 Mill Lane Harrowmere Westshire TW9 3RK</p>
    </div>
  </section>
</body>
</html>
```